Landing Page  Erste Hilfe und Rettung für Veranstaltung
Landing Page Erste Hilfe und Rettung für Veranstaltung
Zielgruppe
Professionelle Erste Hilfe und Rettung für Ihre Veranstaltung
Aufgabenstellung
Design soll zum Instagram Account passen.. wichtig ist die Gelde-Farbe vom RTW! Farbe = RAL 1016

```html
<!DOCTYPE html>
<html lang="de">
<head>
<meta charset="utf-8">
<title>Nordlicht Sanitätsdienst – Erste Hilfe für Veranstaltungen</title>
<link href="https://fonts.googleapis.com/css2?family=Raleway:wght@300;400;500;600;700;800&display=swap" rel="stylesheet">
<style>
:root{
  --navy:#143a86;
  --navy-text:#1c3d8c;
  --yellow:#e9f31b;
  --pale:#e8f3fb;
  --white:#ffffff;
  --deco:rgba(255,255,255,0.12);
}
*{box-sizing:border-box;margin:0;padding:0}
html,body{width:1200px;height:2887px;overflow:hidden;background:var(--white)}
body{position:relative;font-family:'Raleway',sans-serif;color:var(--navy-text)}
.abs{position:absolute}

/* Equipment section */
.team-photo{left:0;top:0;width:605px;height:335px;border-bottom-right-radius:22px;
  background:linear-gradient(160deg,#7f9bb8 0%,#4d6a8f 35%,#27365e 65%,#9a9a92 100%)}
.equip-title{left:662px;top:16px;font-size:31px;font-weight:800;line-height:32px;color:var(--navy-text)}
.yellow-rule{height:4px;width:101px;background:var(--yellow);border-radius:2px}
.equip-text{left:662px;top:131px;width:430px;font-size:14.8px;line-height:18.8px;font-weight:500;letter-spacing:-0.15px}
.tag-row{left:0;width:1200px;display:flex;justify-content:center;gap:16px}
.tag{height:46px;padding:0 22px;border-radius:23px;background:var(--pale);display:flex;align-items:center;font-size:16px;font-weight:500}

/* Booking band */
.booking-band{left:0;top:596px;width:1200px;height:832px;background:var(--navy);overflow:hidden}
.band-decoration{left:88px;top:0;width:198px;height:136px;border-radius:0 0 18px 18px;background:var(--deco)}
.center-text{left:0;width:1200px;text-align:center}
.kicker{font-size:17px;font-weight:400}
.section-title{font-size:28px;font-weight:800}
.step-card{top:953px;width:237px;height:272px;border:2px solid var(--yellow);border-radius:12px}
.step-num{position:absolute;top:-40px;left:50%;margin-left:-37px;width:74px;height:74px;background:var(--yellow);border-radius:8px;
  color:var(--navy);font-size:50px;font-weight:800;display:flex;align-items:center;justify-content:center}
.step-head{position:absolute;top:72px;left:0;width:100%;text-align:center;color:var(--white);font-size:21px;font-weight:800}
.step-text{position:absolute;top:118px;left:33px;width:175px;color:var(--white);font-size:13px;line-height:18.8px}

/* Contact form */
.contact-form{left:320px;top:1300px;width:525px;height:498px;background:var(--white);border-radius:6px;
  box-shadow:0 2px 12px rgba(20,58,134,0.18);overflow:hidden}
.form-header{height:56px;background:var(--pale);display:flex;align-items:center;justify-content:center;font-size:18px}
.label{font-size:12.5px;font-weight:500}
.field{border:1.5px solid var(--navy-text);border-radius:6px;height:41px}
.consent-box{width:28px;height:28px;border:1.5px solid var(--navy-text);border-radius:5px}
.consent-text{font-size:9.6px;line-height:13.5px;width:405px}
.submit{width:152px;height:44px;border-radius:22px;background:var(--yellow);display:flex;align-items:center;justify-content:center;
  font-size:12px;font-weight:700;color:var(--navy);box-shadow:0 2px 6px rgba(0,0,0,0.12)}

/* FAQ */
.faq-heading{left:210px;width:741px;text-align:center}
.faq-item{left:210px;width:741px;border:1.5px solid var(--navy-text);border-radius:6px}
.faq-q{position:absolute;left:19px;top:0;height:44px;display:flex;align-items:center;font-size:16px;font-weight:500}
.faq-icon{position:absolute;right:13px;top:12px}
.faq-a{position:absolute;left:18px;top:57px;width:670px;font-size:13.6px;line-height:18.8px}

/* Footer */
.site-footer{left:0;top:2554px;width:1200px;height:333px;background:var(--navy);border-top-left-radius:22px;border-top-right-radius:22px;color:var(--white)}
.brand{left:120px;top:58px;display:flex;align-items:center;gap:12px}
.brand-mark{width:40px;height:40px;border-radius:50%;border:3px solid var(--white)}
.brand-name{font-size:20px;font-weight:800;line-height:22px}
.foot-col{top:61px}
.foot-head{font-size:16px;font-weight:800;margin-bottom:12px}
.foot-text{font-size:10px;line-height:15.6px;font-weight:400}
.contact-line{display:flex;align-items:center;gap:12px;margin-top:9px;font-size:10px;font-weight:700}
.icon-circle{width:28px;height:28px;border-radius:50%;background:var(--yellow);display:flex;align-items:center;justify-content:center}
.foot-links a{display:block;color:var(--white);text-decoration:none;font-size:10px;margin-bottom:15px}
.legal-bar{left:0;top:2853px;width:1200px;height:34px;background:var(--yellow);border-top-left-radius:18px;border-top-right-radius:18px;
  display:flex;align-items:center;justify-content:center;font-size:8.5px;color:var(--navy)}
</style>
</head>
<body>

<section class="equipment">
  <div class="abs team-photo" role="img" aria-label="Gruppenfoto des Sanitätsteams in dunkelblauen Uniformen bei einer Veranstaltung"></div>
  <h2 class="abs equip-title">Ausgerüstet für alle<br>Eventualitäten</h2>
  <div class="abs yellow-rule" style="left:662px;top:96px"></div>
  <p class="abs equip-text">Unser medizinisches Personal ist bestens ausgerüstet, um in Notfällen schnell und effektiv handeln zu können. Unsere Verbandsrucksäcke enthalten einen Frühdefibrillator (AED), Sauerstoff und alles Wesentliche eines Rettungswagens. Bei Bedarf stellen wir auch Sanitätszelte mit Betten, Sanitätsschränken, Beleuchtung, Infusionsständern und weiterem medizinischen Equipment bereit. Mit unserer professionellen Ausstattung können wir die ersten entscheidenden Minuten bis zum Eintreffen des Notarztes überbrücken und Leben retten.</p>
  <div class="abs tag-row" style="top:371px">
    <span class="tag">Frühdefibrillator (AED)</span><span class="tag">Verbandsrucksäcke</span><span class="tag">Fahrzeuge</span><span class="tag">Sanitätsschränke</span><span class="tag">Infusionsständer</span>
  </div>
  <div class="abs tag-row" style="top:436px">
    <span class="tag" style="padding:0 31px">Beleuchtung</span><span class="tag">Sanitätszelte mit Betten</span><span class="tag" style="padding:0 41px">Sauerstoff</span><span class="tag">uvm.</span>
  </div>
</section>

<section class="abs booking-band">
  <div class="abs band-decoration" role="img" aria-label="Dekoratives Punktmuster"></div>
</section>
<p class="abs center-text kicker" style="top:701px;color:var(--white)">Wie geht’s jetzt weiter?</p>
<h2 class="abs center-text section-title" style="top:736px;color:var(--white)">So kannst du uns buchen:</h2>
<div class="abs yellow-rule" style="left:550px;top:793px"></div>
<p class="abs center-text" style="top:827px;font-size:15.6px;line-height:18.8px;color:var(--white)">Lorem ipsum dolor sit amet, consetetur sadipscing elitr, sed diam nonumy eirmod<br>tempor invidunt ut labore et dolore magna aliquyam erat, sed diam voluptua.</p>

<div class="abs step-card" style="left:202px"><div class="step-num">1</div><h3 class="step-head">Headline</h3><p class="step-text">Lorem ipsum dolor sit amet, consetetur sadipscing elitr, sed diam nonumy eirmod tempor invidunt ut labore et dolore magna aliquyam erat, sed diam voluptua</p></div>
<div class="abs step-card" style="left:482px"><div class="step-num">2</div><h3 class="step-head">Headline</h3><p class="step-text">Lorem ipsum dolor sit amet, consetetur sadipscing elitr, sed diam nonumy eirmod tempor invidunt ut labore et dolore magna aliquyam erat, sed diam voluptua</p></div>
<div class="abs step-card" style="left:761px"><div class="step-num">3</div><h3 class="step-head">Headline</h3><p class="step-text">Lorem ipsum dolor sit amet, consetetur sadipscing elitr, sed diam nonumy eirmod tempor invidunt ut labore et dolore magna aliquyam erat, sed diam voluptua</p></div>

<form class="abs contact-form">
  <div class="form-header">Nimm Kontakt mit uns auf!</div>
  <span class="abs label" style="left:40px;top:86px">Nachname*</span>
  <span class="abs label" style="left:277px;top:86px">Vorname*</span>
  <div class="abs field" style="left:40px;top:108px;width:223px"></div>
  <div class="abs field" style="left:277px;top:108px;width:223px"></div>
  <span class="abs label" style="left:40px;top:163px">E-Mail*</span>
  <span class="abs label" style="left:311px;top:163px">Telefonnummer*</span>
  <div class="abs field" style="left:40px;top:184px;width:255px"></div>
  <div class="abs field" style="left:311px;top:184px;width:189px"></div>
  <span class="abs label" style="left:40px;top:239px">Ihr Anliegen:</span>
  <div class="abs field" style="left:40px;top:261px;width:460px;height:85px"></div>
  <div class="abs consent-box" style="left:40px;top:365px"></div>
  <p class="abs consent-text" style="left:84px;top:365px">Sie erklären sich damit einverstanden, dass Ihre Daten zur Bearbeitung Ihres Anliegens verwendet werden. Weitere Informationen und Widerrufshinweise finden Sie in der Datenschutzerklärung.</p>
  <div class="abs submit" style="left:348px;top:430px">Abenden</div>
</form>

<section class="faq">
  <p class="abs faq-heading kicker" style="top:1888px">Noch was unklar?</p>
  <h2 class="abs faq-heading section-title" style="top:1924px;font-size:29px">Häufig gestellte Fragen</h2>
  <div class="abs yellow-rule" style="left:530px;top:1981px"></div>

  <div class="abs faq-item" style="top:2059px;height:47px"><span class="faq-q">Hier steht eine Frage?</span>
    <svg class="faq-icon" width="20" height="20" viewBox="0 0 20 20"><path d="M7.5 0h5v7.5H20v5h-7.5V20h-5v-7.5H0v-5h7.5z" fill="var(--navy-text)"/></svg></div>
  <div class="abs faq-item" style="top:2116px;height:47px"><span class="faq-q">Hier steht eine etwas längere Frage?</span>
    <svg class="faq-icon" width="20" height="20" viewBox="0 0 20 20"><path d="M7.5 0h5v7.5H20v5h-7.5V20h-5v-7.5H0v-5h7.5z" fill="var(--navy-text)"/></svg></div>
  <div class="abs faq-item" style="top:2174px;height:47px"><span class="faq-q">Lorem ipsum dolor sit amet, consetetur sadipscing elitr, sed diam nonumy eirmod?</span>
    <svg class="faq-icon" width="20" height="20" viewBox="0 0 20 20"><path d="M7.5 0h5v7.5H20v5h-7.5V20h-5v-7.5H0v-5h7.5z" fill="var(--navy-text)"/></svg></div>
  <div class="abs faq-item" style="top:2232px;height:182px"><span class="faq-q">Hier steht eine etwas längere Frage?</span>
    <svg class="faq-icon" width="20" height="20" viewBox="0 0 20 20"><rect x="0" y="7.5" width="20" height="5" fill="var(--navy-text)"/></svg>
    <div class="abs" style="left:18px;top:43px;width:110px;height:2px;background:var(--yellow)"></div>
    <p class="faq-a">Lorem ipsum dolor sit amet, consetetur sadipscing elitr, sed diam nonumy eirmod tempor invidunt ut labore et dolore magna aliquyam erat, sed diam voluptua. At vero eos et accusam et justo duo dolores et ea rebum. Stet clita kasd gubergren, no sea takimata sanctus est Lorem ipsum dolor sit amet. Lorem ipsum dolor sit amet, consetetur sadipscing elitr, sed diam nonumy eirmod tempor invidunt ut labore et dolore magna aliquyam erat, sed diam voluptua. At vero eos et accusam et justo duo dolores et ea rebum. Stet clita kasd gubergren, no sea takimata sanctus est Lorem ipsum dolor sit amet.</p></div>
  <div class="abs faq-item" style="top:2426px;height:47px"><span class="faq-q">Hier steht eine etwas längere Frage?</span>
    <svg class="faq-icon" width="20" height="20" viewBox="0 0 20 20"><path d="M7.5 0h5v7.5H20v5h-7.5V20h-5v-7.5H0v-5h7.5z" fill="var(--navy-text)"/></svg></div>
</section>

<footer class="abs site-footer">
  <div class="abs brand"><span class="brand-mark"></span><span class="brand-name">Nordlicht<br>Sanitätsdienst</span></div>
  <div class="abs foot-col" style="left:412px">
    <h4 class="foot-head">Adresse &amp; Kontakt</h4>
    <p class="foot-text">Nordlicht Rettungsdienst GmbH<br>Lindenweg 12<br>10115 Berlin</p>
    <div style="height:14px"></div>
    <div class="contact-line"><span class="icon-circle"><svg width="14" height="14" viewBox="0 0 24 24"><path d="M6.6 10.8a15.1 15.1 0 0 0 6.6 6.6l2.2-2.2c.3-.3.7-.4 1-.2 1.1.4 2.3.6 3.6.6.6 0 1 .4 1 1V20c0 .6-.4 1-1 1A17 17 0 0 1 3 4c0-.6.4-1 1-1h3.5c.6 0 1 .4 1 1 0 1.3.2 2.5.6 3.6.1.3 0 .7-.2 1z" fill="var(--navy)"/></svg></span>+49 30 555 01 23 45</div>
    <div class="contact-line"><span class="icon-circle"><svg width="14" height="12" viewBox="0 0 24 18"><rect x="1" y="1" width="22" height="16" rx="2" fill="none" stroke="var(--navy)" stroke-width="2"/><path d="M1 2l11 8 11-8" fill="none" stroke="var(--navy)" stroke-width="2"/></svg></span>info@nordlicht-rd.de</div>
    <div class="contact-line"><span class="icon-circle"><span style="width:12px;height:12px;border-radius:50%;border:2px solid var(--navy)"></span></span>@nordlichtsanitaet</div>
  </div>
  <div class="abs foot-col" style="left:638px;width:180px">
    <h4 class="foot-head">Nachhaltigkeit</h4>
    <p class="foot-text">Lorem ipsum dolor sit amet, consetetur sadipscing elitr, sed diam nonumy eirmod tempor invidunt ut labore et dolore magna aliquyam erat, sed diam voluptua. At vero eos et accusam et justo duo dolores et ea rebum. Stet clita kasd gubergren, no sea takimata sanctus est Lorem ipsum dolor sit amet. Lorem ipsum dolor sit amet, consetetur sadipscing elitr.</p>
  </div>
  <div class="abs foot-col foot-links" style="left:864px">
    <h4 class="foot-head">Weitere Links</h4>
    <a href="#">Kontakt</a><a href="#">Impressum</a><a href="#">Datenschutz</a>
  </div>
</footer>
<div class="abs legal-bar">Copyright 2023 © Nordlicht Rettungsdienst GmbH</div>

</body>
</html>
```